practice letterhead

I need a letterhead design for a new company that is a veterinary specialty company. I am conservative. I want it to look professional - not "cutesy"

I need my name, credentials, address, phone number and website/email on it.

My personal information is as follows: Marisol Tedder, DVM, DACVIM (Neurology) Certified Veterinary Pain Practitioner (or CVPP) Certified Canine Rehabilitation Therapist (or CCRT) 4170 Larkfield Hwy Walpole, MA 02081 508-347-6620 marisol.tedder@petspineandcare.com www.petspineandcare.com

```html
<!DOCTYPE html>
<html lang="en">
<head>
<meta charset="utf-8">
<title>Practice Letterhead</title>
<link href="https://fonts.googleapis.com/css2?family=Arimo:wght@700&family=Fjalla+One&display=swap" rel="stylesheet">
<style>
  :root {
    --canvas: #ffffff;
    --page: #ffffff;
    --frame: #0d0d0d;
    --navy: #1b3440;
    --sage: #6a9485;
    --footer-text: #8fb0a4;
  }
  * { margin: 0; padding: 0; box-sizing: border-box; }
  html, body {
    width: 1200px;
    height: 1000px;
    overflow: hidden;
    background: var(--canvas);
  }
  .letterhead {
    position: absolute;
    left: 226px;
    top: 17px;
    width: 749px;
    height: 968px;
    background: var(--page);
    border: 3px solid var(--frame);
    border-radius: 3px;
    overflow: hidden;
  }
  .corner-sweep {
    position: absolute;
    top: 0;
    right: 0;
    width: 310px;
    height: 190px;
  }
  .brand {
    position: absolute;
    left: 64px;
    top: 38px;
    display: flex;
    align-items: center;
    gap: 12px;
  }
  .brand-mark {
    width: 24px;
    height: 24px;
    border-radius: 50%;
    background: var(--sage);
    flex: none;
  }
  .brand-name {
    font-family: "Arimo", Arial, sans-serif;
    font-weight: 700;
    color: var(--sage);
    font-size: 20px;
    line-height: 23px;
    letter-spacing: 0.1px;
  }
  .footer-band {
    position: absolute;
    left: 0;
    bottom: 0;
    width: 100%;
    height: 51px;
    background: var(--navy);
    font-family: "Fjalla One", "Arial Narrow", sans-serif;
    color: var(--footer-text);
    font-size: 12.5px;
    line-height: 15px;
    letter-spacing: 0.2px;
  }
  .footer-name { position: absolute; left: 23px; top: 9px; }
  .footer-phone { position: absolute; left: 317px; top: 9px; }
  .footer-contact { position: absolute; right: 19px; top: 9px; text-align: right; }
</style>
</head>
<body>
  <main class="letterhead">
    <svg class="corner-sweep" viewBox="0 0 310 190" aria-hidden="true">
      <path d="M0 0 H310 V190 C270 60 120 10 0 0 Z" fill="var(--navy)"/>
    </svg>

    <header class="brand">
      <span class="brand-mark" aria-hidden="true"></span>
      <div class="brand-name">
        <div>Harborline Veterinary</div>
        <div>Neurology &amp; Pain Care</div>
        <div>Center</div>
      </div>
    </header>

    <footer class="footer-band">
      <div class="footer-name">Marisol Tedder, DVM<br>DACVIM (Neurology), CVPP, CCRT</div>
      <div class="footer-phone">Phone: 508-347-6620</div>
      <div class="footer-contact">4170 Larkfield Hwy, Walpole, MA 02081<br>www.petspineandcare.com; marisol.tedder@petspineandcare.com</div>
    </footer>
  </main>
</body>
</html>
```